IT Services Postcard

I am looking to update and refresh my existing postcard. I would like to keep all the content it has , but make it more modern and elegant. We are a small boutique IT firm here in Miami, FL in business for 15 years. We support all Brelvanta products. I would like highlight that as well on the postcard- "15 years serving South Florida". I would also like to make the following revisions to the bullet points:Change "Included Email & Virus Protection" to Included Antivirus SoftwareChange "Quorvix Pro Remote Control" to "Secure remote computer access"Add the following bullet point "Included Deskora 480 Backup"You can certainly change the images for the bullet points, and refresh the colors and background as well. I have uploaded a copy of the front and back of my last flyer. I target small to medium size businesses who need a good local IT company they can trust. I look forward to working with you. Thank you.
Target Market(s)
Small Businesses
Industry/Entity Type
It Professional
Colors
Designer to choose colors to be used in the design.
Look and feel

```html
<!DOCTYPE html>
<html lang="en">
<head>
<meta charset="utf-8">
<title>Vantrel Tech Postcard</title>
<link href="https://fonts.googleapis.com/css2?family=Roboto+Condensed:wght@300;400;700&family=Roboto:wght@400;700&display=swap" rel="stylesheet">
<style>
  :root{
    --bg:#e9e6e1;
    --white:#ffffff;
    --ink:#1b1b1b;
    --sky:#1aa3e0;
    --navy:#0b3572;
    --blue:#1763b5;
    --orange:#ff7f11;
    --badge:#1c58a8;
    --muted:#b9c4d3;
  }
  html,body{margin:0;padding:0;width:963px;height:1200px;overflow:hidden;background:var(--bg);}
  .stage{width:1140px;height:1421px;transform:scale(0.8447);transform-origin:0 0;position:relative;font-family:"Roboto Condensed",sans-serif;color:var(--ink);}
  .card{position:absolute;left:64px;width:1014px;background:var(--white);box-shadow:0 3px 10px rgba(0,0,0,.25);overflow:hidden;}
  .card--front{top:35px;height:657px;}
  .card--back{top:720px;height:658px;}
  .brand{position:absolute;left:46px;line-height:1;white-space:nowrap;}
  .brand__name{font-size:40px;font-weight:700;letter-spacing:1px;color:var(--ink);display:flex;align-items:center;gap:10px;}
  .brand__mark{width:13px;height:13px;background:var(--ink);display:inline-block;}
  .brand__sub{font-size:17px;font-weight:700;letter-spacing:.5px;margin-left:110px;margin-top:4px;}
  .tagline{position:absolute;left:373px;top:26px;white-space:nowrap;}
  .tagline__q{font-size:23px;font-weight:400;}
  .tagline__a{font-size:41px;font-weight:300;color:var(--sky);margin-top:2px;}
  .years{position:absolute;right:0;top:35px;width:245px;height:74px;}
  .years svg{position:absolute;inset:0;}
  .years__num{position:absolute;left:60px;top:8px;font-size:38px;font-weight:700;color:var(--white);white-space:nowrap;}
  .years__txt{position:absolute;left:48px;top:48px;font-size:16px;color:var(--white);white-space:nowrap;}
  .services{position:absolute;left:0;top:110px;width:1014px;height:440px;background:linear-gradient(110deg,var(--navy) 0%,var(--blue) 60%,#0e4b98 100%);}
  .services__title{position:absolute;left:92px;top:32px;font-size:25px;font-weight:700;color:var(--white);white-space:nowrap;}
  .feature{position:absolute;display:flex;align-items:center;gap:14px;color:var(--white);font-size:16.5px;font-weight:700;white-space:nowrap;}
  .feature svg{width:30px;height:30px;flex:none;}
  .laptop{position:absolute;left:780px;top:30px;width:234px;height:320px;background:linear-gradient(160deg,#2a2f36 0%,#3a7bd5 45%,#1d4f9c 70%,#5a6068 100%);border-radius:10px 0 0 30px;}
  .other{position:absolute;left:92px;top:345px;color:var(--white);white-space:nowrap;}
  .other__title{font-size:20px;font-weight:700;}
  .other__list{font-size:20px;margin-top:4px;}
  .other__list span{margin-right:18px;}
  .offer{position:absolute;left:0;top:550px;width:710px;height:54px;}
  .offer svg{position:absolute;inset:0;}
  .offer__txt{position:absolute;left:92px;top:12px;font-size:25px;color:var(--white);white-space:nowrap;}
  .offer__txt b{font-weight:700;}
  .badges{position:absolute;display:flex;gap:14px;align-items:center;}
  .badge{width:80px;height:36px;background:var(--badge);border-radius:3px;}
  .badge--line{background:none;border-top:3px solid var(--badge);border-bottom:1px solid var(--muted);height:24px;width:72px;border-radius:0;}
  .badge--plain{background:var(--muted);}
  .contact{position:absolute;left:92px;display:flex;align-items:center;font-size:20px;font-family:"Roboto",sans-serif;white-space:nowrap;}
  .contact__lead{font-family:"Roboto Condensed",sans-serif;font-weight:700;margin-right:52px;white-space:nowrap;}
  .contact__item{display:flex;align-items:center;gap:10px;margin-right:38px;white-space:nowrap;}
  .contact__item svg{width:18px;height:18px;flex:none;}
  .relax{position:absolute;left:354px;top:0;width:480px;height:100px;}
  .relax svg{position:absolute;inset:0;}
  .relax__txt{position:absolute;left:0;right:0;top:32px;text-align:center;font-size:41px;font-weight:300;color:var(--white);white-space:nowrap;}
  .postage{position:absolute;left:875px;top:33px;width:98px;height:78px;border:1.5px solid var(--ink);text-align:center;font-family:"Roboto",sans-serif;font-size:14px;font-weight:700;line-height:17px;padding-top:4px;box-sizing:border-box;white-space:nowrap;}
  .hands{position:absolute;left:0;top:395px;width:330px;height:200px;background:linear-gradient(100deg,#e6c3a6 0%,#d9ad8e 45%,#9fa4ab 70%,#44484e 100%);}
  .rule{position:absolute;left:290px;top:577px;width:724px;height:2px;background:var(--orange);}
</style>
</head>
<body>
<div class="stage">

  <section class="card card--front">
    <div class="brand" style="top:32px">
      <div class="brand__name"><span class="brand__mark"></span>VANTREL TECH</div>
      <div class="brand__sub">MANAGED SERVICES</div>
    </div>
    <div class="tagline">
      <div class="tagline__q">Are Computer Problems frustrating you?</div>
      <div class="tagline__a">We can help!</div>
    </div>
    <div class="years">
      <svg viewBox="0 0 245 74" preserveAspectRatio="none"><polygon points="32,0 245,0 245,74 0,74" fill="var(--sky)"/></svg>
      <div class="years__num">15 YEARS</div>
      <div class="years__txt">SERVING SOUTH FLORIDA</div>
    </div>

    <div class="services">
      <div class="services__title">Our low cost monthly IT Service includes:</div>
      <div class="laptop" role="img" aria-label="Laptop showing a start menu screen"></div>

      <div class="feature" style="left:112px;top:83px"><svg viewBox="0 0 30 30" fill="none" stroke="#fff" stroke-width="1.4"><circle cx="15" cy="15" r="12"/><text x="15" y="20" font-size="12" fill="#fff" stroke="none" text-anchor="middle" font-family="Roboto">24</text></svg>24/7 Monitoring of Servers</div>
      <div class="feature" style="left:112px;top:130px"><svg viewBox="0 0 30 30" fill="none" stroke="#fff" stroke-width="1.4"><path d="M5 5 L25 25 M25 5 L5 25"/><circle cx="7" cy="7" r="3"/></svg>Proactive Desktop &amp; Server Maintenance</div>
      <div class="feature" style="left:112px;top:176px"><svg viewBox="0 0 30 30" fill="none" stroke="#fff" stroke-width="1.4"><path d="M15 15 C10 9 3 11 3 15 C3 19 10 21 15 15 C20 9 27 11 27 15 C27 19 20 21 15 15Z"/></svg>Unlimited Onsite &amp; Remote Support</div>
      <div class="feature" style="left:112px;top:223px"><svg viewBox="0 0 30 30" fill="none" stroke="#fff" stroke-width="1.4"><path d="M15 4 L25 8 C25 17 21 23 15 26 C9 23 5 17 5 8Z"/><path d="M10 14 L14 18 L20 11"/></svg>Included Antivirus SoftwareChange</div>
      <div class="feature" style="left:112px;top:269px"><svg viewBox="0 0 30 30" fill="none" stroke="#fff" stroke-width="1.4"><rect x="4" y="16" width="4" height="10"/><rect x="11" y="12" width="4" height="14"/><rect x="18" y="8" width="4" height="18"/><rect x="25" y="4" width="3" height="22"/></svg>Monthly Network Health Report</div>

      <div class="feature" style="left:470px;top:83px"><svg viewBox="0 0 30 30" fill="none" stroke="#fff" stroke-width="1.4"><circle cx="15" cy="15" r="11"/><ellipse cx="15" cy="15" rx="5" ry="11"/><path d="M4 15 H26 M6 9 H24 M6 21 H24"/></svg>Secure remote computer access</div>
      <div class="feature" style="left:470px;top:130px"><svg viewBox="0 0 30 30" fill="none" stroke="#fff" stroke-width="1.4"><circle cx="8" cy="10" r="3"/><circle cx="15" cy="8" r="3"/><circle cx="22" cy="10" r="3"/><path d="M3 20 Q8 13 13 20 M10 18 Q15 11 20 18 M17 20 Q22 13 27 20"/></svg>Brelvanta Certified Technicians</div>
      <div class="feature" style="left:470px;top:176px"><svg viewBox="0 0 30 30" fill="none" stroke="#fff" stroke-width="1.4"><circle cx="15" cy="15" r="10"/><path d="M15 9 V15 H20"/></svg>Fast Response Times</div>
      <div class="feature" style="left:470px;top:223px"><svg viewBox="0 0 30 30" fill="none" stroke="#fff" stroke-width="1.4"><path d="M8 6 H27 L22 24 H3Z"/><path d="M9 12 H22 M8 16 H20"/></svg>No Long Term Contracts</div>
      <div class="feature" style="left:470px;top:269px"><svg viewBox="0 0 30 30" fill="none" stroke="#fff" stroke-width="1.4"><rect x="4" y="8" width="14" height="19"/><rect x="11" y="3" width="14" height="19"/><path d="M14 8 H22 M14 12 H22 M14 16 H22"/></svg>Included Deskora 480 Backup</div>

      <div class="other">
        <div class="other__title">Other Services Offered:</div>
        <div class="other__list"><span>Onsite/Offsite Backup Solutions</span><span>Deskora 480 Migration</span><span>Norwave Business Voice Edge Installation</span></div>
      </div>
    </div>

    <div class="offer">
      <svg viewBox="0 0 710 54" preserveAspectRatio="none"><polygon points="0,0 705,0 672,54 0,54" fill="var(--orange)"/></svg>
      <div class="offer__txt">Call today and get <b>2 FREE HOURS</b> of onsite service</div>
    </div>
    <div class="badges" style="left:732px;top:553px"><div class="badge badge--line"></div><div class="badge"></div><div class="badge badge--plain" style="width:62px;height:30px"></div></div>

    <div class="contact" style="top:618px">
      <span class="contact__lead">Contact us TODAY!</span>
      <span class="contact__item"><svg viewBox="0 0 18 18"><path d="M4 2 L15 10 L10 10.5 L12.5 16 L10.5 17 L8 11.5 L4 15Z" fill="var(--badge)"/></svg>www.vantreltech.com</span>
      <span class="contact__item"><svg viewBox="0 0 18 18"><rect x="5" y="1" width="8" height="16" rx="2" fill="var(--badge)"/><rect x="7" y="4" width="4" height="5" fill="#fff"/></svg>305.555.0147</span>
      <span class="contact__item"><svg viewBox="0 0 18 18" fill="none" stroke="var(--badge)" stroke-width="1.6"><rect x="1" y="3" width="16" height="12"/><path d="M1 3 L9 10 L17 3"/></svg>support@vantreltech.com</span>
    </div>
  </section>

  <section class="card card--back">
    <div class="brand" style="top:42px">
      <div class="brand__name"><span class="brand__mark"></span>VANTREL TECH</div>
      <div class="brand__sub">MANAGED SERVICES</div>
    </div>
    <div class="relax">
      <svg viewBox="0 0 480 100" preserveAspectRatio="none"><defs><linearGradient id="relaxFill" x1="0" x2="1"><stop offset="0" stop-color="#0e4b98"/><stop offset="1" stop-color="#1a6fc4"/></linearGradient></defs><polygon points="0,0 478,0 412,100 54,100" fill="url(#relaxFill)"/></svg>
      <div class="relax__txt">Relax, we can fix IT!</div>
    </div>
    <div class="postage">U.S. Postage<br>PAID<br>Permit NO<br>4079</div>

    <div class="hands" role="img" aria-label="Hands typing on an open laptop"></div>
    <div class="badges" style="left:695px;top:493px"><div class="badge badge--line"></div><div class="badge"></div><div class="badge badge--plain" style="width:62px;height:30px"></div></div>
    <div class="rule"></div>

    <div class="contact" style="top:606px;left:82px">
      <span class="contact__lead">Contact us TODAY!</span>
      <span class="contact__item"><svg viewBox="0 0 18 18"><path d="M4 2 L15 10 L10 10.5 L12.5 16 L10.5 17 L8 11.5 L4 15Z" fill="var(--badge)"/></svg>www.vantreltech.com</span>
      <span class="contact__item"><svg viewBox="0 0 18 18"><rect x="5" y="1" width="8" height="16" rx="2" fill="var(--badge)"/><rect x="7" y="4" width="4" height="5" fill="#fff"/></svg>305.555.0147</span>
      <span class="contact__item"><svg viewBox="0 0 18 18" fill="none" stroke="var(--badge)" stroke-width="1.6"><rect x="1" y="3" width="16" height="12"/><path d="M1 3 L9 10 L17 3"/></svg>support@vantreltech.com</span>
    </div>
  </section>

</div>
</body>
</html>
```